Business Card for Yachting Management Company

Need a business card design for a new yachting project management company. Attached is the logo for the company.
Our clients are large yacht owners and captains.
Design must be in the style of the logo. Modern, elegant.

Example of data to show:
Peter Hollis
Project Manager
(+34) 612 738 104
peter@quorvane.net
Quorvane Management - Meridel Tower, Office 22 - KRB - Palma de Mallorca

The data above will have to be changed (by me) for the different people in the company over the next years.

Will be printed using PrintNova (Lustre Card Series). They provide these guidelines for the size:
"the actual size of the card is 1050 x 600 pixels. However, the full bleed size is 1083 x 633 pixels, and the safe printing area is 1008 x 558 pixels."

```html
<!DOCTYPE html>
<html lang="en">
<head>
<meta charset="utf-8">
<title>Quorvane Management – Business Card</title>
<link href="https://fonts.googleapis.com/css2?family=Michroma&family=Poppins:wght@400;600&display=swap" rel="stylesheet">
<style>
  :root {
    --navy: #0a2a66;
    --navy-deep: #061d4a;
    --navy-light: #0d3a8a;
    --brand-blue: #0672c4;
    --mark-blue: #0b74c8;
    --grey: #7d7d7d;
    --ink: #3a3a3a;
    --white: #ffffff;
    --page: #ffffff;
  }
  * { box-sizing: border-box; margin: 0; padding: 0; }
  html, body { width: 1200px; height: 2400px; overflow: hidden; background: var(--page); }
  .sheet { position: relative; width: 1200px; height: 2400px; }

  .card {
    position: absolute; left: 128px; width: 944px; height: 550px; overflow: hidden;
    box-shadow: 0 4px 10px rgba(0,0,0,0.25);
  }
  .card--front { top: 580px; }
  .card--back  { top: 1270px; background: var(--white); }

  .card__backdrop { position: absolute; inset: 0; width: 100%; height: 100%; }

  .brand-name {
    position: absolute; font-family: "Michroma", sans-serif; color: var(--mark-blue);
    text-align: center; line-height: 1.25; text-transform: uppercase;
  }
  .card--front .brand-name { left: 0; width: 944px; top: 180px; font-size: 50px; letter-spacing: 6px; }
  .card--back .brand-name { left: 0; width: 475px; top: 210px; font-size: 27px; letter-spacing: 3px; }

  .web-band {
    position: absolute; left: 0; width: 944px; top: 478px; text-align: center;
    font-family: "Michroma", sans-serif; font-size: 26px; color: var(--white);
    letter-spacing: 14px; font-weight: 400;
  }

  .navy-panel { position: absolute; left: 0; top: 0; width: 475px; height: 550px; }
  .icon-strip {
    position: absolute; left: 449px; top: 107px; width: 50px; height: 328px;
    background: var(--brand-blue);
  }
  .icon { position: absolute; left: 9px; width: 32px; height: 32px; }

  .person__name {
    position: absolute; left: 520px; top: 113px; font-family: "Michroma", sans-serif;
    font-size: 25px; color: var(--grey); letter-spacing: 0.5px; white-space: nowrap;
  }
  .person__role {
    position: absolute; left: 520px; top: 146px; font-family: "Poppins", sans-serif;
    font-weight: 600; font-size: 20px; color: var(--ink);
  }
  .contact {
    position: absolute; left: 520px; font-family: "Poppins", sans-serif; font-size: 21px;
    color: var(--ink); line-height: 26px; letter-spacing: 0.3px;
  }
  .contact--phone { top: 220px; }
  .contact--address { top: 272px; }
  .contact--email { top: 340px; }
  .contact--web { top: 396px; }
</style>
</head>
<body>
<main class="sheet">

  <section class="card card--front" aria-label="Card front">
    <svg class="card__backdrop" viewBox="0 0 944 550" preserveAspectRatio="none" aria-hidden="true">
      <defs>
        <linearGradient id="frontNavy" x1="0" y1="0" x2="1" y2="1">
          <stop offset="0" stop-color="var(--navy-light)"/>
          <stop offset="1" stop-color="var(--navy-deep)"/>
        </linearGradient>
      </defs>
      <rect width="944" height="550" fill="url(#frontNavy)"/>
      <polygon points="0,0 330,0 944,520 944,550 700,550 0,-40" fill="#000" opacity="0.10"/>
      <polygon points="330,0 560,0 944,330 944,520" fill="#000" opacity="0.08"/>
      <polygon points="560,0 680,0 944,220 944,330" fill="#fff" opacity="0.03"/>
      <polygon points="0,60 0,300 250,550 480,550" fill="#000" opacity="0.10"/>
      <polygon points="0,296 152,457 792,457 944,278 944,550 0,550" fill="var(--brand-blue)"/>
    </svg>
    <div class="brand-name">Quorvane<br>Management</div>
    <div class="web-band">WWW.QUORVANE.NET</div>
  </section>

  <section class="card card--back" aria-label="Card back">
    <svg class="navy-panel" viewBox="0 0 475 550" preserveAspectRatio="none" aria-hidden="true">
      <defs>
        <linearGradient id="backNavy" x1="0" y1="0" x2="1" y2="1">
          <stop offset="0" stop-color="var(--navy-light)"/>
          <stop offset="1" stop-color="var(--navy-deep)"/>
        </linearGradient>
      </defs>
      <rect width="475" height="550" fill="url(#backNavy)"/>
      <polygon points="0,0 210,0 475,270 475,420" fill="#000" opacity="0.10"/>
      <polygon points="210,0 330,0 475,150 475,270" fill="#000" opacity="0.07"/>
      <polygon points="0,40 0,260 290,550 420,550" fill="#000" opacity="0.10"/>
      <polygon points="0,260 0,400 150,550 290,550" fill="#000" opacity="0.06"/>
    </svg>
    <div class="brand-name">Quorvane<br>Management</div>

    <div class="icon-strip">
      <svg class="icon icon--person" style="top:7px" viewBox="0 0 32 32" aria-hidden="true">
        <circle cx="16" cy="16" r="14" fill="none" stroke="#fff" stroke-width="2"/>
        <circle cx="16" cy="12" r="5" fill="none" stroke="#fff" stroke-width="2"/>
        <path d="M7 26c2-5 5-7 9-7s7 2 9 7" fill="none" stroke="#fff" stroke-width="2"/>
      </svg>
      <svg class="icon icon--phone" style="top:112px" viewBox="0 0 32 32" aria-hidden="true">
        <path d="M9 5l4 5-2.5 3c1.5 3.5 4 6 7.5 7.5L21 18l5 4-2 4c-9 0-18-9-18-18z" fill="#fff"/>
        <path d="M18 6a8 8 0 0 1 8 8M18 10a4 4 0 0 1 4 4" fill="none" stroke="#fff" stroke-width="2"/>
      </svg>
      <svg class="icon icon--pin" style="top:170px" viewBox="0 0 32 32" aria-hidden="true">
        <path d="M16 3a9 9 0 0 1 9 9c0 7-9 17-9 17S7 19 7 12a9 9 0 0 1 9-9z" fill="#fff"/>
        <circle cx="16" cy="12" r="3.5" fill="var(--brand-blue)"/>
      </svg>
      <svg class="icon icon--mail" style="top:231px" viewBox="0 0 32 32" aria-hidden="true">
        <rect x="3" y="8" width="26" height="17" fill="#fff"/>
        <path d="M3 8l13 10L29 8M3 25l10-9M29 25l-10-9" fill="none" stroke="var(--brand-blue)" stroke-width="1.6"/>
      </svg>
      <svg class="icon icon--globe" style="top:287px" viewBox="0 0 32 32" aria-hidden="true">
        <circle cx="16" cy="16" r="12" fill="#fff"/>
        <path d="M4 16h24M16 4v24M6 10h20M6 22h20" stroke="var(--brand-blue)" stroke-width="1.5" fill="none"/>
        <ellipse cx="16" cy="16" rx="5.5" ry="12" fill="none" stroke="var(--brand-blue)" stroke-width="1.5"/>
      </svg>
    </div>

    <h1 class="person__name">PETER HOLLIS</h1>
    <p class="person__role">Project Manager</p>
    <p class="contact contact--phone">(+34) 612 738 104</p>
    <p class="contact contact--address">Meridel Tower, Office 22 -<br>KRB - Palma de Mallorca</p>
    <p class="contact contact--email">peter@quorvane.net</p>
    <p class="contact contact--web">www.quorvane.net</p>
  </section>

</main>
</body>
</html>
```